Tradeshow Exhibit Company needs Stationary design

We would like to have a upper and lower header designed for the use in our quotes and invoices. We will need to be able to drop it into programs like Microsoft word and Apple Pages etc. My guess would be that it needs to be a JPEG or something of that nature.

Just looking or a 1Inch Tittle Bar with a simple design like a flowing ribbon of colors or something . The Tittle bar should include.

Marlow Displays
T-517-263-0948
www.MarlowDisplays.example

And our Logo of course. Our colors are Black Grays, Silver's White.

Target Market(s)

Professional Marketing coordinators for large companies

Industry/Entity Type

It Company

Requirements
Must have
• Keep it professional

```html
<!DOCTYPE html>
<html lang="en">
<head>
<meta charset="utf-8">
<title>Marlow Displays Letterhead</title>
<link rel="stylesheet" href="https://fonts.googleapis.com/css2?family=Cinzel:wght@400;700&display=swap">
<style>
  :root {
    --paper: #ffffff;
    --ink: #2b2b2b;
    --ink-soft: #555555;
    --rule: #c9c9c9;
    --ribbon-edge: #c0392b;
    --ribbon-light: #fff7c2;
    --ribbon-gold: #f3c232;
    --ribbon-orange: #ee8a22;
    --divider: #8a7a4a;
  }
  * { margin: 0; padding: 0; box-sizing: border-box; }
  html, body { width: 849px; height: 1200px; overflow: hidden; background: var(--paper); }
  .sheet { position: relative; width: 849px; height: 1200px; background: var(--paper); font-family: "Cinzel", serif; color: var(--ink); }

  .masthead { position: absolute; top: 96px; left: 0; width: 100%; text-align: center; }
  .masthead .brand-name { font-size: 30px; font-weight: 400; letter-spacing: 1px; color: var(--ink); }

  .title-ribbon { position: absolute; left: 42px; top: 603px; width: 742px; height: 127px; }
  .title-ribbon svg { position: absolute; inset: 0; }
  .ribbon-brand { position: absolute; left: 0; top: 0; width: 354px; height: 127px; display: flex; align-items: center; justify-content: center; }
  .ribbon-brand .brand-name { font-size: 27px; font-weight: 400; color: var(--ink); }
  .ribbon-contact { position: absolute; left: 372px; top: 34px; font-weight: 700; color: var(--ink); }
  .ribbon-contact .phone { font-size: 19px; letter-spacing: 0.5px; margin-bottom: 8px; }
  .ribbon-contact .web { font-size: 15px; letter-spacing: 0.3px; }

  .footer-line { position: absolute; left: 150px; right: 150px; top: 1118px; border-top: 1px solid var(--rule); }
  .footer-contact { position: absolute; top: 1130px; left: 0; width: 100%; text-align: center; font-size: 15px; color: var(--ink-soft); letter-spacing: 0.5px; }
  .footer-contact .sep { margin: 0 8px; }
</style>
</head>
<body>
<div class="sheet">
  <header class="masthead">
    <div class="brand-name">Marlow Displays</div>
  </header>

  <section class="title-ribbon">
    <svg width="742" height="127" viewBox="0 0 742 127" aria-hidden="true">
      <defs>
        <linearGradient id="ribbonFill" x1="0" y1="0" x2="1" y2="0">
          <stop offset="0" stop-color="var(--ribbon-gold)"/>
          <stop offset="0.22" stop-color="var(--ribbon-light)"/>
          <stop offset="0.5" stop-color="var(--ribbon-gold)"/>
          <stop offset="1" stop-color="var(--ribbon-orange)"/>
        </linearGradient>
      </defs>
      <polygon points="1,1 741,1 705,63.5 741,126 1,126" fill="url(#ribbonFill)" stroke="var(--ribbon-edge)" stroke-width="2"/>
      <line x1="354" y1="18" x2="354" y2="109" stroke="var(--divider)" stroke-width="1.5"/>
    </svg>
    <div class="ribbon-brand"><span class="brand-name">Marlow Displays</span></div>
    <div class="ribbon-contact">
      <div class="phone">T-517-263-0948</div>
      <div class="web">www.MarlowDisplays.example</div>
    </div>
  </section>

  <div class="footer-line"></div>
  <footer class="footer-contact">T-517-263-0948<span class="sep">|</span>www.MarlowDisplays.example</footer>
</div>
</body>
</html>
```